PowerPoint Design BROM

I have now selected the logo for my consultancy company. I need some innovative design for my Powerpoint slides. The audience is senior executives in international banks predominantly in Asia, but also in the Middle East, Africa and Latin America.
My company advises them on solutions to be able to grow their business.
This is my main means of hooking the clients and it is crucial to the success of my business.
I will update the file to a vector file in a few hours.

I am looking for a complete template.

Senior hard nosed executives in international Banks

```html
<!DOCTYPE html>
<html lang="en">
<head>
<meta charset="utf-8">
<title>BROM – Presentation Template</title>
<link href="https://fonts.googleapis.com/css2?family=Jura:wght@400;500;600&family=Carlito:wght@400;700&display=swap" rel="stylesheet">
<style>
  :root {
    --page: #ffffff;
    --slide-bg-1: #fafafa;
    --slide-bg-2: #e4e4e4;
    --band: #7dcfd1;
    --teal: #5ec9cf;
    --teal-dark: #27a6ab;
    --teal-light: #8ad3d8;
    --green: #95d69c;
    --yellow: #e6ee1b;
    --lime: #c3dc45;
    --leaf: #86cf7a;
    --ink: #333333;
    --grey: #777777;
    --line: #9a9a9a;
    --row-a: #d7eff0;
    --row-b: #eaf7f7;
  }
  * { box-sizing: border-box; margin: 0; padding: 0; }
  html, body { width: 1200px; height: 724px; overflow: hidden; background: var(--page); }
  body { position: relative; font-family: "Jura", "Segoe UI", sans-serif; color: var(--ink); }

  .slide {
    position: absolute; width: 385px; height: 290px; overflow: hidden;
    background: radial-gradient(ellipse at 35% 40%, var(--slide-bg-1) 0%, #efefef 60%, var(--slide-bg-2) 100%);
    box-shadow: 1px 2px 4px rgba(0,0,0,.35);
  }
  .slide--title   { left: 8px;   top: 45px; }
  .slide--chevron { left: 405px; top: 45px; }
  .slide--donut   { left: 803px; top: 45px; }
  .slide--bars    { left: 8px;   top: 388px; }
  .slide--mixed   { left: 405px; top: 388px; }
  .slide--table   { left: 803px; top: 388px; }

  .slide__band {
    position: absolute; left: 0; top: 0; width: 100%; height: 50px;
    background: var(--band); color: #fff; padding: 14px 11px 0;
    font-size: 18px; font-weight: 500; letter-spacing: .2px;
  }
  .slide__band--two-line { font-size: 15px; line-height: 20px; padding-top: 4px; }

  .brand { position: absolute; display: flex; align-items: center; gap: 5px; color: var(--grey); font-weight: 500; }
  .brand__dot { border-radius: 50%; background: var(--leaf); }
  .brand--footer { left: 9px; bottom: 10px; font-size: 9px; }
  .brand--footer .brand__dot { width: 13px; height: 13px; }
  .brand--cover { right: 14px; top: 16px; font-size: 15px; color: #6f6f6f; }
  .brand--cover .brand__dot { width: 30px; height: 30px; }

  .footer-meta { position: absolute; bottom: 12px; font-size: 6px; color: var(--teal); }

  /* cover */
  .cover__art {
    position: absolute; left: -10px; top: 0; width: 250px; height: 290px; border-radius: 50%;
    background: radial-gradient(circle at 50% 45%, #f3f3f3 0%, #e6e6e6 70%, rgba(230,230,230,0) 72%);
  }
  .cover__title { position: absolute; right: 14px; top: 126px; text-align: right; color: var(--teal-light); font-size: 18px; line-height: 23px; }
  .cover__subtitle { position: absolute; right: 14px; top: 193px; color: #8a8a8a; font-size: 11px; }

  /* chevrons */
  .chevron-row { position: absolute; left: 15px; top: 72px; width: 360px; height: 190px; }
  .chevron-card { position: absolute; top: 70px; width: 100px; height: 113px; padding: 5px 6px;
    background: linear-gradient(#efefef, #d2d2d2); border: 1px solid #bcbcbc;
    font-size: 7.2px; line-height: 10.2px; color: #333; }

  /* donut + bars */
  .chart-title { position: absolute; width: 100%; text-align: center; font-family: "Carlito", sans-serif; }
  .legend { position: absolute; font-family: "Carlito", sans-serif; font-size: 8.5px; color: #333; }
  .legend li { list-style: none; display: flex; align-items: center; gap: 4px; line-height: 15px; }
  .legend i { width: 6px; height: 6px; display: inline-block; }

  /* mixed */
  .panel { position: absolute; border: 1px dashed #a9d8da; }
  .bullets { padding: 10px 10px 0 14px; font-size: 6.2px; line-height: 9.6px; color: #7a7a7a; }
  .bullets li { list-style: none; position: relative; margin-bottom: 5.5px; padding-left: 12px; }
  .bullets li::before { content: ""; position: absolute; left: 0; top: 4.5px; width: 5px; height: 1px; background: var(--lime); }

  /* table */
  .table-title { position: absolute; top: 96px; width: 100%; text-align: center; color: var(--teal); font-size: 10px; }
  .data-table { position: absolute; left: 55px; top: 122px; width: 257px; border-collapse: collapse;
    font-family: "Carlito", sans-serif; font-size: 9px; text-align: center; }
  .data-table th { background: var(--teal); color: #fff; font-weight: 400; height: 16px; border: 1px solid #fff; }
  .data-table td { height: 15.5px; border: 1px solid #fff; background: var(--row-a); }
  .data-table tr:nth-child(even) td { background: var(--row-b); }
</style>
</head>
<body>

<!-- Cover -->
<section class="slide slide--title">
  <div class="cover__art" role="img" aria-label="Faint grey sphere formed of flowing wave lines"></div>
  <div class="brand brand--cover"><span class="brand__dot"></span>BROM</div>
  <h1 class="cover__title" style="font-weight:400">Lorem ipsum<br>dolor sit amet</h1>
  <p class="cover__subtitle">Nam non mi velit</p>
</section>

<!-- Chevron slide -->
<section class="slide slide--chevron">
  <h2 class="slide__band" style="font-weight:500">Chevron Slide</h2>
  <div class="chevron-row">
    <svg width="360" height="80" viewBox="0 0 360 80">
      <defs>
        <linearGradient id="chevA" x1="0" y1="0" x2="0" y2="1"><stop offset="0" stop-color="#a9e0ae"/><stop offset="1" stop-color="#7fcc88"/></linearGradient>
        <linearGradient id="chevB" x1="0" y1="0" x2="0" y2="1"><stop offset="0" stop-color="#8ddbdf"/><stop offset="1" stop-color="#55c3c9"/></linearGradient>
        <linearGradient id="chevC" x1="0" y1="0" x2="0" y2="1"><stop offset="0" stop-color="#4fbec2"/><stop offset="1" stop-color="#1e9ea3"/></linearGradient>
      </defs>
      <polygon points="0,0 105,0 120,25 105,50 0,50 15,25" fill="url(#chevA)"/>
      <polygon points="118,0 223,0 238,25 223,50 118,50 133,25" fill="url(#chevB)"/>
      <polygon points="235,0 340,0 355,25 340,50 235,50 250,25" fill="url(#chevC)"/>
      <g font-family="Jura, sans-serif" font-size="12" fill="#fff" text-anchor="middle">
        <text x="62" y="30">Category A</text>
        <text x="180" y="30">Category B</text>
        <text x="297" y="30">Category C</text>
      </g>
      <g stroke-width="1">
        <line x1="62" y1="50" x2="62" y2="70" stroke="#8fd49a"/><circle cx="62" cy="70" r="2.5" fill="#8fd49a"/>
        <line x1="176" y1="50" x2="176" y2="70" stroke="#6fcfd4"/><circle cx="176" cy="70" r="2.5" fill="#6fcfd4"/>
        <line x1="298" y1="50" x2="298" y2="70" stroke="#2aa9ad"/><circle cx="298" cy="70" r="2.5" fill="#2aa9ad"/>
      </g>
    </svg>
    <p class="chevron-card" style="left:9px">Lorem ipsum dolor sit amet, consectetur adipiscing elit. Mauris a pulvinar mi. Duis cursus varius aliquam. Duis nec quam eget lectus bibendum venenatis vel nec elit. Quisque id nisl at massa consectetur iaculis id eu mauris.</p>
    <p class="chevron-card" style="left:126px">Lorem ipsum dolor sit amet, consectetur adipiscing elit. Mauris a pulvinar mi. Duis cursus varius aliquam. Duis nec quam eget lectus bibendum venenatis vel nec elit. Quisque id nisl at massa consectetur iaculis id eu mauris.</p>
    <p class="chevron-card" style="left:248px">Lorem ipsum dolor sit amet, consectetur adipiscing elit. Mauris a pulvinar mi. Duis cursus varius aliquam. Duis nec quam eget lectus bibendum venenatis vel nec elit. Quisque id nisl at massa consectetur iaculis id eu mauris.</p>
  </div>
  <div class="brand brand--footer"><span class="brand__dot"></span>BROM</div>
  <span class="footer-meta" style="left:83px">04-07-2013</span>
  <span class="footer-meta" style="left:235px">Confidential</span>
  <span class="footer-meta" style="left:364px">7</span>
</section>

<!-- Donut slide -->
<section class="slide slide--donut">
  <h2 class="slide__band slide__band--two-line" style="font-weight:500">Lorem ipsum dolor sit amet, consectetur adipiscing</h2>
  <p class="chart-title" style="top:78px;left:0;width:365px;font-size:10px;font-weight:700">Graphic Title</p>
  <svg style="position:absolute;left:104px;top:105px" width="120" height="120" viewBox="0 0 120 120">
    <g transform="rotate(-90 60 60)" fill="none" stroke-width="30">
      <circle cx="60" cy="60" r="45" stroke="#5ec9cf" stroke-dasharray="166.8 282.74"/>
      <circle cx="60" cy="60" r="45" stroke="#e6ee1b" stroke-dasharray="48.07 282.74" stroke-dashoffset="-166.8"/>
      <circle cx="60" cy="60" r="45" stroke="#b9d83a" stroke-dasharray="33.93 282.74" stroke-dashoffset="-214.87"/>
      <circle cx="60" cy="60" r="45" stroke="#86cf7a" stroke-dasharray="33.93 282.74" stroke-dashoffset="-248.8"/>
    </g>
    <g font-family="Carlito, sans-serif" font-size="8" fill="#fff" text-anchor="middle">
      <text x="105" y="80">59%</text>
      <text x="19" y="89">17%</text>
      <text x="17" y="48">12%</text>
      <text x="43" y="23">12%</text>
    </g>
  </svg>
  <ul class="legend" style="left:272px;top:134px">
    <li><i style="background:#5ec9cf"></i>1st Qtr</li>
    <li><i style="background:#e6ee1b"></i>2nd Qtr</li>
    <li><i style="background:#b9d83a"></i>3rd Qtr</li>
    <li><i style="background:#86cf7a"></i>4th Qtr</li>
  </ul>
  <div class="brand brand--footer"><span class="brand__dot"></span>BROM</div>
</section>

<!-- Bar chart slide -->
<section class="slide slide--bars">
  <h2 class="slide__band" style="font-weight:500">Chart slide 1</h2>
  <p class="chart-title" style="top:65px;color:var(--teal);font-size:10px;font-family:Jura,sans-serif">Chart title</p>
  <svg style="position:absolute;left:0;top:0" width="385" height="260" viewBox="0 0 385 260">
    <g>
      <!-- Category 1 -->
      <rect x="80" y="121.4" width="14" height="94.6" fill="#5ec9cf"/>
      <rect x="94" y="163.2" width="14" height="52.8" fill="#e6ee1b"/>
      <rect x="108" y="172" width="14" height="44" fill="#c3dc45"/>
      <!-- Category 2 -->
      <rect x="140" y="161" width="14" height="55" fill="#5ec9cf"/>
      <rect x="154" y="119.2" width="14" height="96.8" fill="#e6ee1b"/>
      <rect x="168" y="172" width="14" height="44" fill="#c3dc45"/>
      <!-- Category 3 -->
      <rect x="200" y="139" width="14" height="77" fill="#5ec9cf"/>
      <rect x="214" y="176.4" width="14" height="39.6" fill="#e6ee1b"/>
      <rect x="228" y="150" width="14" height="66" fill="#c3dc45"/>
      <!-- Category 4 -->
      <rect x="260" y="117" width="14" height="99" fill="#5ec9cf"/>
      <rect x="274" y="154.4" width="14" height="61.6" fill="#e6ee1b"/>
      <rect x="288" y="106" width="14" height="110" fill="#c3dc45"/>
    </g>
    <line x1="72" y1="216" x2="312" y2="216" stroke="#888" stroke-width="1"/>
    <g font-family="Carlito, sans-serif" font-size="8" fill="#333" text-anchor="middle">
      <text x="87" y="118">4,3</text><text x="101" y="160">2,4</text><text x="115" y="169">2</text>
      <text x="147" y="158">2,5</text><text x="161" y="116">4,4</text><text x="175" y="169">2</text>
      <text x="207" y="136">3,5</text><text x="221" y="173">1,8</text><text x="235" y="147">3</text>
      <text x="267" y="114">4,5</text><text x="281" y="151">2,8</text><text x="295" y="103">5</text>
      <text x="101" y="229">Category 1</text><text x="161" y="229">Category 2</text>
      <text x="221" y="229">Category 3</text><text x="281" y="229">Category 4</text>
    </g>
    <g font-family="Carlito, sans-serif" font-size="7.5" fill="#333">
      <rect x="137" y="237" width="5" height="5" fill="#5ec9cf"/><text x="144" y="242">Series 1</text>
      <rect x="176" y="237" width="5" height="5" fill="#e6ee1b"/><text x="183" y="242">Series 2</text>
      <rect x="215" y="237" width="5" height="5" fill="#c3dc45"/><text x="222" y="242">Series 3</text>
    </g>
  </svg>
  <div class="brand brand--footer"><span class="brand__dot"></span>BROM</div>
</section>

<!-- Several charts + text -->
<section class="slide slide--mixed">
  <h2 class="slide__band" style="font-weight:500">Several charts + text slide</h2>
  <div class="panel" style="left:12px;top:55px;width:181px;height:105px">
    <svg width="180" height="104" viewBox="0 0 180 104">
      <g font-family="Carlito, sans-serif" font-size="6" fill="#333" text-anchor="end">
        <text x="24" y="90">0</text><text x="24" y="77">1</text><text x="24" y="63">2</text><text x="24" y="50">3</text>
        <text x="24" y="37">4</text><text x="24" y="23">5</text><text x="24" y="10">6</text>
      </g>
      <line x1="30" y1="88" x2="140" y2="88" stroke="#888" stroke-width=".6"/>
      <line x1="30" y1="8" x2="30" y2="88" stroke="#888" stroke-width=".6"/>
      <g font-family="Carlito, sans-serif" font-size="6" fill="#333" text-anchor="middle">
        <text x="42" y="97">2010</text><text x="69" y="97">2011</text><text x="96" y="97">2012</text><text x="123" y="97">2013</text>
      </g>
      <g fill="none" stroke-width="1.4">
        <polyline points="42,30.7 69,54.7 96,41.3 123,28" stroke="#5ec9cf"/>
        <polyline points="42,56 69,29.3 96,64 123,50.7" stroke="#e6ee1b"/>
        <polyline points="42,61.3 69,61.3 96,48 123,21.3" stroke="#c3dc45"/>
      </g>
      <g font-family="Carlito, sans-serif" font-size="6" fill="#333">
        <line x1="148" y1="41" x2="156" y2="41" stroke="#5ec9cf" stroke-width="1.4"/><text x="159" y="43">A</text>
        <line x1="148" y1="50" x2="156" y2="50" stroke="#e6ee1b" stroke-width="1.4"/><text x="159" y="52">B</text>
        <line x1="148" y1="59" x2="156" y2="59" stroke="#c3dc45" stroke-width="1.4"/><text x="159" y="61">C</text>
      </g>
    </svg>
  </div>
  <div class="panel" style="left:12px;top:162px;width:181px;height:113px">
    <svg width="180" height="112" viewBox="0 0 180 112">
      <line x1="30" y1="6" x2="30" y2="88" stroke="#888" stroke-width=".6"/>
      <g>
        <rect x="30" y="10" width="80" height="4" fill="#c3dc45"/><rect x="30" y="14" width="46" height="4" fill="#e6ee1b"/><rect x="30" y="18" width="66" height="4" fill="#5ec9cf"/>
        <rect x="30" y="31" width="55" height="4" fill="#c3dc45"/><rect x="30" y="35" width="33" height="4" fill="#e6ee1b"/><rect x="30" y="39" width="64" height="4" fill="#5ec9cf"/>
        <rect x="30" y="52" width="37" height="4" fill="#c3dc45"/><rect x="30" y="56" width="81" height="4" fill="#e6ee1b"/><rect x="30" y="60" width="46" height="4" fill="#5ec9cf"/>
        <rect x="30" y="73" width="37" height="4" fill="#c3dc45"/><rect x="30" y="77" width="44" height="4" fill="#e6ee1b"/><rect x="30" y="81" width="79" height="4" fill="#5ec9cf"/>
      </g>
      <g font-family="Carlito, sans-serif" font-size="6" fill="#333" text-anchor="end">
        <text x="26" y="18">2013</text><text x="26" y="39">2012</text><text x="26" y="60">2011</text><text x="26" y="81">2010</text>
      </g>
      <g font-family="Carlito, sans-serif" font-size="6" fill="#333" text-anchor="middle">
        <text x="30" y="97">0</text><text x="67" y="97">2</text><text x="103" y="97">4</text><text x="140" y="97">6</text>
      </g>
      <g font-family="Carlito, sans-serif" font-size="6" fill="#333">
        <rect x="150" y="37" width="4" height="4" fill="#c3dc45"/><text x="156" y="41">C</text>
        <rect x="150" y="46" width="4" height="4" fill="#e6ee1b"/><text x="156" y="50">B</text>
        <rect x="150" y="55" width="4" height="4" fill="#5ec9cf"/><text x="156" y="59">A</text>
      </g>
    </svg>
  </div>
  <div class="panel" style="left:205px;top:55px;width:173px;height:222px">
    <ul class="bullets">
      <li>Lorem ipsum dolor sit amet, consectetur adipiscing elit. Proin in velit facilisis libero consectetur adipiscing.</li>
      <li>Aenean congue euismod erat, eu adipiscing dui gravida in.</li>
      <li>Donec vehicula tellus sit amet est aliquet ac pretium lacus aliquam.</li>
      <li>Suspendisse potenti. Integer est nunc, dignissim ac sagittis sit amet, pretium sit amet libero.</li>
      <li>Cras id nibh et ipsum ultrices pretium. Curabitur id leo tellus, a convallis justo. In turpis magna, aliquam ut consequat et, tempor ultrices mauris.</li>
    </ul>
  </div>
  <div class="brand brand--footer"><span class="brand__dot"></span>BROM</div>
</section>

<!-- Table slide -->
<section class="slide slide--table">
  <h2 class="slide__band" style="font-weight:500">Table slide</h2>
  <p class="table-title">Table Title</p>
  <table class="data-table">
    <thead><tr><th>Category A</th><th>Category B</th><th>Category C</th><th>Category D</th></tr></thead>
    <tbody>
      <tr><td>111.222</td><td>111.333</td><td>111.444</td><td>111.999</td></tr>
      <tr><td>222.333</td><td>222.444</td><td>222.333</td><td>222.333</td></tr>
      <tr><td>333.444</td><td>333.555</td><td>333.888</td><td>333.999</td></tr>
      <tr><td>444.555</td><td>444.222</td><td>444.777</td><td>444.555</td></tr>
      <tr><td>555.222</td><td>555.777</td><td>555.888</td><td>555.222</td></tr>
    </tbody>
  </table>
  <div class="brand brand--footer"><span class="brand__dot"></span>BROM</div>
</section>

</body>
</html>
```